Mezzanine Floor Manufacturer looking for a new business card design

We manufacture mezzanine floors and are providers of racking systems. We provide a range of items/services - simple rack repairs , full warehouse fit outs , manufacturer and install mezzanine floors , partitioning and large turnkey projects. Recently had a new website - www.corvane-shelving.co.uk and would like our business cards updating aswell . Our current card is single sided in the old logo colours (pdf attached) and needs updating.

Target Market(s)

We deal with large projects/ multi national companies and also smaller projects and companies throughout the UK ranging from a single warehouse to a large multi site company.

Industry/Entity Type

Business

Contact Information for Business Card

Will have job title,tel no's, email ,website address etc like example pdf

Requirements
Must have
• Hi - needs to use the colours of the logo & new website. Card needs to be professional

```html
<!DOCTYPE html>
<html lang="en">
<head>
<meta charset="utf-8">
<title>Corvane Business Card</title>
<link href="https://fonts.googleapis.com/css2?family=Open+Sans:wght@400;600;700;800&display=swap" rel="stylesheet">
<style>
  :root {
    --brand-red: #c61f28;
    --charcoal: #2b2b2d;
    --card-dark: #262628;
    --ink: #4a4a4a;
    --paper: #ffffff;
    --page: #e9e7e4;
  }
  * { box-sizing: border-box; margin: 0; padding: 0; }
  html, body {
    width: 1200px; height: 900px; overflow: hidden;
    background: var(--page);
    font-family: "Open Sans", Arial, sans-serif;
  }
  .stage { position: relative; width: 1200px; height: 900px; }
  .card {
    position: absolute; width: 620px; height: 365px;
    box-shadow: 0 8px 24px rgba(0,0,0,.18);
    overflow: hidden;
  }

  /* Back of card */
  .card-back { left: 520px; top: 50px; background: var(--card-dark); color: var(--paper); }
  .back-brand {
    position: absolute; left: 40px; top: 130px;
    display: flex; align-items: center; gap: 16px;
  }
  .brand-dot { width: 58px; height: 58px; border-radius: 50%; background: var(--brand-red); }
  .back-brand .brand-name { font-size: 50px; font-weight: 800; color: var(--paper); letter-spacing: .5px; }
  .services {
    position: absolute; left: 395px; top: 78px;
    list-style: none; font-size: 19px; font-weight: 600; line-height: 26px;
  }
  .services li::before { content: "•"; margin-right: 10px; }

  /* Front of card */
  .card-front { left: 60px; top: 465px; background: var(--paper); }
  .front-decor { position: absolute; inset: 0; }
  .contact-name {
    position: absolute; left: 78px; top: 32px;
    font-size: 22px; font-weight: 700; color: var(--brand-red);
  }
  .contact-role {
    position: absolute; left: 78px; top: 62px;
    font-size: 14px; color: var(--ink);
  }
  .address {
    position: absolute; left: 40px; top: 108px;
    font-size: 15px; line-height: 21px; color: var(--ink); font-style: normal;
  }
  .contact-list {
    position: absolute; left: 40px; top: 178px;
    list-style: none; font-size: 15px; line-height: 21px; color: var(--ink);
  }
  .contact-list li { display: flex; align-items: center; gap: 8px; }
  .contact-list svg { width: 12px; height: 12px; fill: var(--brand-red); }
  .front-brand {
    position: absolute; left: 360px; top: 125px;
    display: flex; align-items: center; gap: 12px;
  }
  .front-brand .brand-dot { width: 44px; height: 44px; }
  .front-brand .brand-name { font-size: 40px; font-weight: 800; color: var(--brand-red); }
</style>
</head>
<body>
<main class="stage">

  <section class="card card-back" aria-label="Card back">
    <div class="back-brand">
      <span class="brand-dot"></span>
      <span class="brand-name">Corvane</span>
    </div>
    <ul class="services">
      <li>Mezzanine Floors</li>
      <li>Cantilever Racking</li>
      <li>Pallet Racking</li>
      <li>Safety Barriers</li>
      <li>Longspan Shelving</li>
      <li>Steel Shelving</li>
      <li>Partitioning</li>
      <li>Turnkey Projects</li>
    </ul>
  </section>

  <section class="card card-front" aria-label="Card front">
    <svg class="front-decor" width="620" height="365" viewBox="0 0 620 365" aria-hidden="true">
      <polygon points="0,22 42,22 20,50 0,50" fill="var(--charcoal)"/>
      <polygon points="46,22 72,22 50,50 24,50" fill="var(--brand-red)"/>
      <polygon points="0,288 300,288 285,306 0,306" fill="var(--charcoal)"/>
      <polygon points="300,312 620,312 620,365 262,365" fill="var(--brand-red)"/>
    </svg>

    <h1 class="contact-name">Daniel Hartley</h1>
    <p class="contact-role">Technical Sales</p>

    <address class="address">
      Twelve Mill Lane<br>
      Brookfield Business Park<br>
      Alfreton, Derbyshire DE55 4QR
    </address>

    <ul class="contact-list">
      <li><svg viewBox="0 0 12 12"><rect x="3" y="0" width="6" height="12" rx="1"/></svg>07700 900412</li>
      <li><svg viewBox="0 0 12 12"><path d="M2 1h3l1 3-2 1a7 7 0 0 0 3 3l1-2 3 1v3l-1 1C5 11 1 7 1 2z"/></svg>01632 960481</li>
      <li><svg viewBox="0 0 12 12"><path d="M0 2h12v8H0z M0 2l6 5 6-5" /></svg>01632 960592</li>
      <li><svg viewBox="0 0 12 12"><circle cx="6" cy="6" r="6"/></svg>daniel@corvane-shelving.co.uk</li>
      <li>www.corvane-shelving.co.uk</li>
    </ul>

    <div class="front-brand">
      <span class="brand-dot"></span>
      <span class="brand-name">Corvane</span>
    </div>
  </section>

</main>
</body>
</html>
```